Expo Program Guide Design and Logo for Lantern Grove Gatherings

First, we are looking for a new logo for "Lantern Grove Gatherings" similar in feel to our other brands, Harvest Kite Fest and Bright Path Showcase. Attached is a graphic showing the three current logos.

Second we are looking for a new overall layout for our holistic living expo program guides that apply this new logo. Each 16-24 page guide has the following sections that need to have templates created that carry out the same look/feel.

a) front and back covers (similar in feel to the Denver Guide attached page 1 or Chicago page 1)
b) Welcome page (similar to the Chicago Guide attached page 3)
c) Expo lecture overview page (similar in feel to the Chicago Guide attached page 7, should only allow for 4 presentation rooms and be vertical to the page.)
d) Left detail page of presentations (similar in feel to the Chicago Guide attached page 34)
e) Right detail page of presentations (similar in feel to the Chicago Guide attached page 35)
f) Detail page for exhibitors (similar in feel to the Chicago Guide attached page 24)
g) Detail page for featured presenters (similar in feel to the Chicago Guide attached page 12)
f) Detail page for secondary featured presenters (similar in feel to the Chicago Guide attached page 15)

Target Market(s)

Casual female 25-54 with interest in holistic subjects

Requirements
Must have
• Logo should have horizontal aspect ratio.

Although samples may be in AI, PSD or PDF, we must have the templates in InDesign native files at the conclusion of the project for all pages of the guide.

Final logo should be vector based.

```html
<!DOCTYPE html>
<html lang="en">
<head>
<meta charset="utf-8">
<title>Lantern Grove Gatherings – Denver Expo Guide Cover</title>
<link rel="stylesheet" href="https://fonts.googleapis.com/css2?family=Arimo:wght@400;700&family=Anton&family=Tinos:ital@0;1&display=swap">
<style>
  :root {
    --lime: #cde23a;
    --white: #ffffff;
    --orange: #f39a5c;
    --ink: #1c1c22;
    --purple: #a35ab4;
    --yellow: #f0e34a;
    --magenta: #c83c8c;
    --pink: #e83a6e;
    --seal-green: #7fae4a;
    --seal-cream: #f6f3e2;
    --seal-gold: #d8c04a;
    --sky-top: #163a52;
    --sky-mid: #6f8a86;
    --sun-glow: #f4b43a;
    --sun-core: #fde27a;
    --sea: #3a2a10;
    --shore: #120c06;
  }
  * { margin: 0; padding: 0; box-sizing: border-box; }
  html, body { width: 927px; height: 1200px; overflow: hidden; background: #000; }
  .cover {
    position: relative;
    width: 927px;
    height: 1200px;
    overflow: hidden;
    font-family: "Arimo", Arial, sans-serif;
  }
  .cover-photo {
    position: absolute;
    inset: 0;
    background:
      radial-gradient(ellipse 520px 420px at 470px 820px, var(--sun-core) 0%, var(--sun-glow) 35%, rgba(230,140,40,0.6) 60%, rgba(0,0,0,0) 100%),
      linear-gradient(180deg, var(--sky-top) 0%, #2a5068 25%, var(--sky-mid) 45%, #c99a40 68%, #d88a22 80%, var(--sea) 90%, var(--shore) 100%);
  }
  .cover-text { position: absolute; text-shadow: 2px 3px 4px rgba(0,0,0,0.55); }

  .brand {
    top: 52px; left: 70px; right: 70px;
    text-align: center;
    font-family: "Anton", "Arimo", sans-serif;
    font-weight: 400;
    color: var(--lime);
    line-height: 1;
    letter-spacing: 2px;
  }
  .brand-line-1 { display: block; font-size: 96px; }
  .brand-line-2 { display: block; font-size: 62px; text-align: right; margin-top: 8px; }

  .venue { left: 58px; top: 530px; }
  .venue-city { font-weight: 700; font-size: 80px; color: var(--magenta); letter-spacing: -1px; line-height: 1; }
  .venue-hall { font-weight: 700; font-size: 29px; color: var(--white); margin-top: 4px; }
  .venue-detail { font-weight: 400; font-size: 25px; color: var(--white); line-height: 1.35; margin-top: 10px; }

  .topics { left: 636px; top: 412px; line-height: 1; }
  .topic-health { font-weight: 400; font-size: 38px; color: var(--orange); line-height: 1.05; }
  .topic-growth { font-weight: 700; font-size: 44px; color: var(--white); line-height: 1.05; margin-top: 14px; }
  .topic-meta { font-weight: 400; font-size: 35px; color: var(--ink); margin-top: 16px; text-shadow: none; }

  .stats { left: 640px; top: 720px; line-height: 1; }
  .stat-number { font-weight: 700; font-size: 84px; letter-spacing: -2px; }
  .stat-number.exhibitors { color: var(--purple); }
  .stat-number.readers { color: var(--pink); margin-top: 16px; }
  .stat-label { font-weight: 700; font-size: 37px; }
  .stat-label.exhibitors { color: var(--yellow); margin-top: 2px; }
  .stat-label.readers { color: var(--white); line-height: 1.05; margin-top: 4px; }

  .reading-seal { position: absolute; left: 58px; top: 935px; width: 200px; height: 200px; }
  .reading-seal .seal-ring-text { font-family: "Tinos", serif; font-style: italic; font-size: 17px; fill: #4a5a2a; }
  .reading-seal .seal-price { font-family: "Arimo", sans-serif; font-weight: 700; font-size: 40px; fill: var(--seal-green); }
</style>
</head>
<body>
<main class="cover">
  <div class="cover-photo" role="img" aria-label="Photograph: silhouette of a woman dancing barefoot on the beach with arms raised and hair flying, against a golden sunset over the sea"></div>

  <h1 class="cover-text brand">
    <span class="brand-line-1">LANTERN GROVE</span>
    <span class="brand-line-2">GATHERINGS</span>
  </h1>

  <section class="cover-text venue">
    <div class="venue-city">DENVER</div>
    <div class="venue-hall">HARBOR EXCHANGE HALL</div>
    <div class="venue-detail">Sept 6-8<br>Admission $5</div>
  </section>

  <section class="cover-text topics">
    <div class="topic-health">NATURAL<br>HEALTH</div>
    <div class="topic-growth">Personal<br>Growth</div>
    <div class="topic-meta">Metaphysics</div>
  </section>

  <section class="cover-text stats">
    <div class="stat-number exhibitors">220</div>
    <div class="stat-label exhibitors">Exhibitors</div>
    <div class="stat-number readers">90</div>
    <div class="stat-label readers">Readers<br>&amp; Healers</div>
  </section>

  <svg class="reading-seal" viewBox="0 0 200 200" aria-label="Readings and Headings, $20 for 20 minutes">
    <defs>
      <path id="seal-arc-top" d="M40,100 A60,60 0 0,1 160,100"/>
      <path id="seal-arc-bottom" d="M45,108 A55,55 0 0,0 155,108"/>
    </defs>
    <polygon fill="var(--seal-green)" points="100,2 112,14 128,6 136,21 153,18 156,35 173,37 170,54 185,62 178,77 192,88 181,100 192,112 178,123 185,138 170,146 173,163 156,165 153,182 136,179 128,194 112,186 100,198 88,186 72,194 64,179 47,182 44,165 27,163 30,146 15,138 22,123 8,112 19,100 8,88 22,77 15,62 30,54 27,37 44,35 47,18 64,21 72,6 88,14"/>
    <circle cx="100" cy="100" r="80" fill="var(--seal-gold)"/>
    <circle cx="100" cy="100" r="76" fill="var(--seal-cream)"/>
    <text class="seal-ring-text"><textPath href="#seal-arc-top" startOffset="50%" text-anchor="middle">Readings &amp; Headings</textPath></text>
    <text class="seal-price" x="100" y="114" text-anchor="middle">$20</text>
    <text class="seal-ring-text"><textPath href="#seal-arc-bottom" startOffset="50%" text-anchor="middle" dominant-baseline="hanging">For 20 Min</textPath></text>
  </svg>
</main>
</body>
</html>
```